Business Card Design for Law firm - already have logo

Now that we have a logo, we need a business card design - our logo is attached -it is salaryman font if that helps - we would like a file that can be uploaded to cardquill (www.cardquill-example.com) using the logo and with the following information on it:
Quenby Law Firm, P.C.
Delwyn Quenby, Esq.
5817 SW 19th Ave.
Larkmoor, OR 97099
971.555.0142 phone
971.555.0187 fax
del@quenby-example.net
Chatline: delquenby
Talkwire: delwyn.quenby@mailbox-example.com
Target Market(s)
our business cards are distributed to corporate executives, technology professionals and healthcare providers
Industry/Entity Type
Business
Look and feel

```html
<!DOCTYPE html>
<html lang="en">
<head>
<meta charset="utf-8">
<title>Quenby Law Firm – Business Card</title>
<link rel="stylesheet" href="https://fonts.googleapis.com/css2?family=Maven+Pro:wght@400;500&display=swap">
<style>
  :root {
    --backdrop: #d9d9d9;
    --card-white: #ffffff;
    --band-dark: #2b2a29;
    --logo-ink: #2b2a29;
    --name-ink: #3a3a3a;
    --band-text: #e8e8e8;
  }
  * { margin: 0; padding: 0; box-sizing: border-box; }
  html, body {
    width: 1200px;
    height: 900px;
    overflow: hidden;
    background: var(--backdrop);
    font-family: "Maven Pro", sans-serif;
  }
  .card {
    position: absolute;
    left: 100px;
    top: 164px;
    width: 1000px;
    height: 572px;
    background: var(--card-white);
    box-shadow: 0 10px 30px rgba(0,0,0,0.18);
    overflow: hidden;
  }
  .brand {
    position: absolute;
    top: 88px;
    left: 0;
    width: 100%;
    display: flex;
    justify-content: center;
    align-items: center;
    gap: 26px;
  }
  .brand-square {
    width: 64px;
    height: 64px;
    background: var(--logo-ink);
  }
  .brand-name {
    font-size: 84px;
    font-weight: 400;
    letter-spacing: 18px;
    color: var(--logo-ink);
    line-height: 1;
  }
  .holder-name {
    position: absolute;
    top: 262px;
    width: 100%;
    text-align: center;
    font-size: 30px;
    font-weight: 400;
    letter-spacing: 1.5px;
    color: var(--name-ink);
  }
  .contact-band {
    position: absolute;
    left: 0;
    bottom: 0;
    width: 100%;
    height: 240px;
    background: var(--band-dark);
    display: flex;
    flex-direction: column;
    justify-content: center;
    align-items: center;
    gap: 14px;
  }
  .contact-line {
    font-size: 22px;
    letter-spacing: 1px;
    color: var(--band-text);
    white-space: nowrap;
  }
  .sep { padding: 0 10px; }
</style>
</head>
<body>
  <div class="card">
    <div class="brand">
      <span class="brand-square"></span>
      <span class="brand-name">QUENBY</span>
    </div>
    <div class="holder-name">DELWYN QUENBY, ESQ.</div>
    <div class="contact-band">
      <p class="contact-line">T: 555.555.0142<span class="sep">|</span>F: 555.555.0187<span class="sep">|</span>E: del@quenby-example.net</p>
      <p class="contact-line">Quenby Law Firm, P.C.<span class="sep">|</span>5817 SW 19th Ave.<span class="sep">|</span>Larkmoor, OR 97099</p>
      <p class="contact-line">Chatline: delquenby<span class="sep">|</span>Talkwire: delwyn.quenby@mailbox-example.com</p>
    </div>
  </div>
</body>
</html>
```